Auto Detailing Facility Needs Facebook Cover Photo

Looking for a beautiful Facebook cover photo using our logo and a photo, including our business information. Does not have to use the photo provided but the logo must be in there. I want an eye-catching cover photo that promotes the luxury brand.

Website: www.glossbayauto.com
Phone: 603-555-0147
Address: 412 Lower Maple Rd Unit B-3 Harborview, NH 02091

Industry/Entity Type

Automotive

Colors

Designer to choose colors to be used in the design.

```html
<!DOCTYPE html>
<html lang="en">
<head>
<meta charset="utf-8">
<title>Gloss Bay Auto – Cover</title>
<link rel="stylesheet" href="https://fonts.googleapis.com/css2?family=Bebas+Neue&family=Montserrat:wght@300;600&display=swap">
<style>
  :root {
    --stage: #c3c9d6;
    --ink: #000000;
    --white: #ffffff;
    --accent: #f7941d;
    --paint-red: #8a1420;
    --paint-teal: #1d6f78;
    --glow: #c9652a;
  }
  * { margin: 0; padding: 0; box-sizing: border-box; }
  html, body { width: 1200px; height: 869px; overflow: hidden; background: var(--stage); }
  .cover {
    position: absolute; left: 0; top: 206px; width: 1200px; height: 456px;
    background: var(--ink); overflow: hidden;
  }
  .car-photo {
    position: absolute; left: 380px; top: 0; width: 820px; height: 456px;
    background:
      radial-gradient(ellipse 40% 45% at 78% 40%, var(--paint-red) 0%, rgba(138,20,32,0.5) 50%, transparent 100%),
      radial-gradient(ellipse 35% 40% at 45% 55%, var(--paint-teal) 0%, rgba(29,111,120,0.4) 55%, transparent 100%),
      radial-gradient(ellipse 45% 35% at 20% 30%, var(--glow) 0%, rgba(201,101,42,0.3) 50%, transparent 100%),
      linear-gradient(90deg, var(--ink) 0%, rgba(0,0,0,0.2) 35%, rgba(0,0,0,0.3) 100%);
  }
  .car-photo::after {
    content: ""; position: absolute; inset: 0;
    background: linear-gradient(90deg, var(--ink) 0%, transparent 30%), linear-gradient(0deg, rgba(0,0,0,0.7) 0%, transparent 30%);
  }
  .headline {
    position: absolute; left: 53px; top: 46px;
    font-family: "Bebas Neue", sans-serif; font-weight: 400; color: var(--white); line-height: 0.9;
  }
  .headline .line-one { font-size: 72px; letter-spacing: -1px; display: block; }
  .headline .line-two { display: block; margin-top: 2px; }
  .headline .small { font-size: 44px; letter-spacing: -0.5px; }
  .headline .highlight { font-size: 56px; color: var(--accent); letter-spacing: -0.5px; }
  .contact {
    position: absolute; left: 62px; top: 200px; list-style: none;
    font-family: "Montserrat", sans-serif; font-weight: 600; font-size: 18px;
    color: var(--white); letter-spacing: -0.3px;
  }
  .contact li { display: flex; align-items: flex-start; margin-bottom: 10px; line-height: 23px; }
  .contact svg { width: 16px; height: 16px; margin: 4px 10px 0 0; flex: none; fill: var(--accent); }
  .brand {
    position: absolute; right: 55px; top: 372px;
    font-family: "Montserrat", sans-serif; font-weight: 300; font-size: 26px;
    color: var(--white); letter-spacing: 2px;
  }
</style>
</head>
<body>
  <section class="cover">
    <div class="car-photo" role="img" aria-label="Photo of a glossy red and teal sports car on a road at sunset"></div>
    <h1 class="headline">
      <span class="line-one">Bringing Detailing</span>
      <span class="line-two"><span class="small">To Your </span><span class="highlight">Doorstep</span></span>
    </h1>
    <ul class="contact">
      <li>
        <svg viewBox="0 0 16 16"><circle cx="8" cy="8" r="7" fill="none" stroke="var(--accent)" stroke-width="1.6"/><path d="M1 8h14M8 1c3 3 3 11 0 14M8 1c-3 3-3 11 0 14" fill="none" stroke="var(--accent)" stroke-width="1.2"/></svg>
        www.glossbayauto.com
      </li>
      <li>
        <svg viewBox="0 0 16 16"><path d="M3.5 1.5l2.5 0 1.2 3.2-1.6 1.3c.8 1.7 2.2 3.1 3.9 3.9l1.3-1.6 3.2 1.2 0 2.5c0 .8-.7 1.5-1.5 1.5C6.8 13.5 2 8.7 2 3c0-.8.7-1.5 1.5-1.5z"/></svg>
        603-555-0147
      </li>
      <li>
        <svg viewBox="0 0 16 16"><path d="M8 0.5C5 0.5 2.8 2.8 2.8 5.7 2.8 9.6 8 15.5 8 15.5s5.2-5.9 5.2-9.8C13.2 2.8 11 0.5 8 0.5zm0 7.2a2 2 0 110-4 2 2 0 010 4z"/></svg>
        <span>412 Lower Maple Rd Unit B-3 Harborview,<br>NH 02091</span>
      </li>
    </ul>
    <div class="brand">GLOSS BAY AUTO</div>
  </section>
</body>
</html>
```